Business card for hedge fund
Vornelle Capital Management
Project: Business card for hedge fund
Business card for hedge fund - Financial Services
Creative Brief
Professional
Wanrudee Halvorsen
Chief Operating Officer
wanru.halvorsen@vornellecap.example
2 additional names: Martin Gaskell, Portfolio Manager p: +1-555-382-4719 e-mail: martin.gaskell@vornellecap.example Jia Luo, Portfolio Manager p: +852-5123-9046 e: jia.luo@vornellecap.example No address to be included

```html
<!DOCTYPE html>
<html lang="en">
<head>
<meta charset="utf-8">
<title>Vornelle Capital Management – Business Card</title>
<link rel="stylesheet" href="https://fonts.googleapis.com/css2?family=Open+Sans:wght@400;600;700&display=swap">
<style>
  :root {
    --page: #e6e6e6;
    --card-top: #ffffff;
    --card-top-shade: #e4e4e4;
    --dark-1: #444444;
    --dark-2: #1e1e1e;
    --orange-1: #f39a12;
    --orange-2: #fdd267;
    --brand-ink: #4b4b4b;
    --light-ink: #ffffff;
    --icon-bg: #ffffff;
    --icon-ink: #333333;
  }
  html, body {
    margin: 0;
    width: 1200px;
    height: 770px;
    overflow: hidden;
    background: var(--page);
    font-family: "Open Sans", Arial, sans-serif;
  }
  .card {
    position: relative;
    width: 1200px;
    height: 770px;
    border-radius: 44px;
    overflow: hidden;
    background: radial-gradient(ellipse at 50% 25%, var(--card-top) 40%, var(--card-top-shade) 100%);
  }
  .card__waves {
    position: absolute;
    inset: 0;
    width: 1200px;
    height: 770px;
  }
  .brand {
    position: absolute;
    top: 128px;
    left: 0;
    width: 1200px;
    text-align: center;
    color: var(--brand-ink);
    font-weight: 400;
  }
  .brand__name {
    font-size: 78px;
    letter-spacing: 8px;
    line-height: 1;
  }
  .brand__tagline {
    margin-top: 10px;
    font-size: 27px;
    letter-spacing: 3px;
    line-height: 1;
  }
  .contacts {
    position: absolute;
    left: 52px;
    top: 470px;
    margin: 0;
    padding: 0;
    list-style: none;
  }
  .contacts__item {
    display: flex;
    align-items: center;
    height: 50px;
    color: var(--light-ink);
    font-size: 22px;
  }
  .contacts__icon {
    width: 30px;
    height: 30px;
    margin-right: 16px;
    flex: none;
  }
  .person {
    position: absolute;
    right: 50px;
    top: 605px;
    text-align: right;
    color: var(--light-ink);
  }
  .person__name {
    font-size: 29px;
    font-weight: 700;
    line-height: 1.2;
  }
  .person__title {
    font-size: 23px;
    font-weight: 400;
    margin-top: 6px;
  }
</style>
</head>
<body>
<div class="card">
  <svg class="card__waves" viewBox="0 0 1200 770" aria-hidden="true">
    <defs>
      <linearGradient id="darkBand" x1="0" y1="0" x2="0" y2="1">
        <stop offset="0" stop-color="var(--dark-1)"/>
        <stop offset="1" stop-color="var(--dark-2)"/>
      </linearGradient>
      <linearGradient id="orangeSwoosh" x1="0" y1="0" x2="1" y2="0">
        <stop offset="0" stop-color="var(--orange-1)"/>
        <stop offset="0.5" stop-color="var(--orange-2)"/>
        <stop offset="1" stop-color="var(--orange-1)"/>
      </linearGradient>
    </defs>
    <path class="wave wave--shadow" fill="#cfcfcf"
      d="M0,395 C280,410 470,470 640,455 C850,435 1030,360 1200,300 L1200,330 C1030,390 850,470 640,490 C450,505 280,450 0,430 Z"/>
    <path class="wave wave--dark" fill="url(#darkBand)"
      d="M0,420 C280,440 460,505 650,490 C860,470 1040,390 1200,330 L1200,770 L0,770 Z"/>
    <path class="wave wave--orange" fill="url(#orangeSwoosh)"
      d="M0,330 C250,345 430,410 620,410 C820,410 1000,350 1200,275 L1200,292 C1000,375 820,440 620,442 C420,444 250,372 0,345 Z"/>
    <path class="wave wave--orange-thin" fill="url(#orangeSwoosh)"
      d="M120,372 C330,395 480,448 660,446 C860,442 1020,380 1170,318 C1020,392 860,458 660,462 C470,466 320,410 120,372 Z"/>
  </svg>

  <div class="brand">
    <div class="brand__name">VORNELLE</div>
    <div class="brand__tagline">CAPITAL MANAGEMENT</div>
  </div>

  <ul class="contacts">
    <li class="contacts__item">
      <svg class="contacts__icon" viewBox="0 0 30 30" aria-hidden="true"><circle cx="15" cy="15" r="14" fill="var(--icon-bg)"/><path d="M10 8 l3 0 l1.5 4 l-2 1.5 c1 2 2.5 3.5 4.5 4.5 l1.5-2 l4 1.5 l0 3 c-7 1-14-6-12.5-12.5 z" fill="var(--icon-ink)"/></svg>
      +1-555-796-0182
    </li>
    <li class="contacts__item">
      <svg class="contacts__icon" viewBox="0 0 30 30" aria-hidden="true"><circle cx="15" cy="15" r="14" fill="var(--icon-bg)"/><rect x="10" y="7" width="10" height="16" rx="2" fill="var(--icon-ink)"/><rect x="11.5" y="9" width="7" height="10" fill="var(--icon-bg)"/></svg>
      +1-555-567-0143
    </li>
    <li class="contacts__item">
      <svg class="contacts__icon" viewBox="0 0 30 30" aria-hidden="true"><circle cx="15" cy="15" r="14" fill="var(--icon-bg)"/><rect x="8" y="12" width="14" height="10" rx="1.5" fill="var(--icon-ink)"/><rect x="11" y="7" width="8" height="6" fill="var(--icon-ink)"/><rect x="11" y="16" width="8" height="2" fill="var(--icon-bg)"/></svg>
      +1-555-654-0176
    </li>
    <li class="contacts__item">
      <svg class="contacts__icon" viewBox="0 0 30 30" aria-hidden="true"><circle cx="15" cy="15" r="14" fill="var(--icon-bg)"/><rect x="7.5" y="10" width="15" height="10" rx="1" fill="var(--icon-ink)"/><path d="M8 10.5 l7 5.5 l7-5.5" fill="none" stroke="var(--icon-bg)" stroke-width="1.5"/></svg>
      wanru.halvorsen@vornellecap.example
    </li>
    <li class="contacts__item">
      <svg class="contacts__icon" viewBox="0 0 30 30" aria-hidden="true"><circle cx="15" cy="15" r="14" fill="var(--icon-bg)"/><circle cx="15" cy="15" r="8" fill="none" stroke="var(--icon-ink)" stroke-width="1.8"/><ellipse cx="15" cy="15" rx="3.5" ry="8" fill="none" stroke="var(--icon-ink)" stroke-width="1.5"/><path d="M7 15 h16" stroke="var(--icon-ink)" stroke-width="1.5"/></svg>
      www.vornellecap.example
    </li>
  </ul>

  <div class="person">
    <div class="person__name">Wanrudee Halvorsen</div>
    <div class="person__title">Chief Operating Officer</div>
  </div>
</div>
</body>
</html>
```